Marlowe Holdings LLC - Business Cards

Need the following information on the cards:

Name: Dean R Vossler
Title: Chief Executive Manager

Business address:
412 N Ridgeview Lane #118
Linden Hollow, Il 60412

Phone: (555) 555-0148 - Business
KPV FFL license number: 5-21-xxx-xx-xx-04519
Email: dean.vossler@marloweholdingsffl.com

Target Market(s)

Firearm owners

Industry/Entity Type

Firearms industry,

Contact Information for Business Card

Contact number, name and title, web page address, email, business address and kpv license number,

Requirements
Must have
• Name, title, business address, phone numbers, KPV license numbers, web page address and email address.
Nice to have
• Cellphone number,

```html
<!DOCTYPE html>
<html lang="en">
<head>
<meta charset="utf-8">
<title>Marlowe Holdings LLC – Business Cards</title>
<link rel="stylesheet" href="https://fonts.googleapis.com/css2?family=Alfa+Slab+One&family=Montserrat:wght@500;700&family=Roboto:wght@400&display=swap">
<style>
  :root {
    --backdrop: #141414;
    --paper: #e9e9e9;
    --paper-shade: #d6d6d6;
    --brand-red: #d01c24;
    --ink: #111111;
    --ink-soft: #1b1b1b;
    --white: #ffffff;
  }
  * { box-sizing: border-box; margin: 0; padding: 0; }
  html, body { width: 1200px; height: 880px; overflow: hidden; background: var(--backdrop); }
  .canvas { position: relative; width: 1200px; height: 880px; }

  .card {
    position: absolute; left: 296px; width: 608px; height: 348px; overflow: hidden;
    background: radial-gradient(ellipse at 30% 20%, var(--paper) 0%, var(--paper-shade) 100%);
  }
  .card--front { top: 81px; }
  .card--back { top: 452px; }

  .band { position: absolute; }
  .front-band-red { left: 0; top: 78px; width: 200px; height: 193px; background: var(--brand-red); }
  .front-band-black { right: 0; top: 78px; width: 208px; height: 193px; background: var(--ink); }

  .brand-seal {
    position: absolute; border-radius: 50%; background: var(--paper);
    display: flex; align-items: center; justify-content: center; text-align: center;
    font-family: "Montserrat", sans-serif; font-weight: 700; color: var(--brand-red);
    letter-spacing: 0.04em; line-height: 1.2;
  }
  .brand-seal--front { left: 167px; top: 38px; width: 275px; height: 275px; font-size: 26px; }
  .brand-seal--back { left: 106px; top: 130px; width: 180px; height: 180px; font-size: 17px; }

  .back-band-black {
    left: 160px; top: 110px; width: 448px; height: 220px;
    background: var(--ink); border-radius: 60px 0 0 60px;
  }
  .back-band-red { left: 0; top: 134px; width: 200px; height: 172px; background: var(--brand-red); }

  .holder-name {
    position: absolute; top: 32px; width: 100%; text-align: center;
    font-family: "Alfa Slab One", serif; font-size: 33px; color: var(--brand-red);
    letter-spacing: 0.01em; line-height: 1.2;
  }
  .holder-title {
    position: absolute; top: 74px; width: 100%; text-align: center;
    font-family: "Montserrat", sans-serif; font-weight: 500; font-size: 18px;
    letter-spacing: 0.16em; color: var(--ink-soft);
  }

  .contact-list { position: absolute; left: 318px; top: 139px; list-style: none; }
  .contact-item { display: flex; align-items: flex-start; height: 41px; }
  .contact-item:last-child { height: 50px; }
  .contact-icon {
    width: 30px; height: 30px; border-radius: 50%; background: var(--brand-red);
    display: flex; align-items: center; justify-content: center; margin-right: 12px; flex: none;
  }
  .contact-text { font-family: "Roboto", sans-serif; color: var(--white); padding-top: 1px; }
  .contact-label { display: block; font-size: 9px; color: var(--brand-red); line-height: 1.2; }
  .contact-value { display: block; font-size: 11.5px; line-height: 1.3; }
</style>
</head>
<body>
<main class="canvas">

  <section class="card card--front" aria-label="Card front">
    <div class="band front-band-red"></div>
    <div class="band front-band-black"></div>
    <div class="brand-seal brand-seal--front">MARLOWE<br>HOLDINGS LLC</div>
  </section>

  <section class="card card--back" aria-label="Card back">
    <h1 class="holder-name">DEAN R VOSSLER</h1>
    <p class="holder-title">CHIEF EXECUTIVE MANAGER</p>
    <div class="band back-band-black"></div>
    <div class="band back-band-red"></div>
    <div class="brand-seal brand-seal--back">MARLOWE<br>HOLDINGS LLC</div>

    <ul class="contact-list">
      <li class="contact-item">
        <span class="contact-icon">
          <svg width="16" height="16" viewBox="0 0 24 24"><path fill="#fff" d="M6.6 10.8a15.1 15.1 0 0 0 6.6 6.6l2.2-2.2c.3-.3.7-.4 1-.2 1.1.4 2.3.6 3.6.6.6 0 1 .4 1 1V20c0 .6-.4 1-1 1A17 17 0 0 1 3 4c0-.6.4-1 1-1h3.5c.6 0 1 .4 1 1 0 1.3.2 2.5.6 3.6.1.3 0 .7-.2 1z"/></svg>
        </span>
        <span class="contact-text"><span class="contact-label">Business</span><span class="contact-value">(555) 555-0148</span></span>
      </li>
      <li class="contact-item">
        <span class="contact-icon">
          <svg width="16" height="16" viewBox="0 0 24 24"><path fill="#fff" d="M2 11 22 3l-4 18-6-5-3 4v-6l9-9-11 7z"/></svg>
        </span>
        <span class="contact-text"><span class="contact-label">Email</span><span class="contact-value">dean.vossler@marloweholdingsffl.com</span></span>
      </li>
      <li class="contact-item">
        <span class="contact-icon">
          <svg width="16" height="16" viewBox="0 0 24 24"><rect x="3" y="5" width="18" height="14" rx="1.5" fill="none" stroke="#fff" stroke-width="2"/><path d="M6 10h6M6 14h6" stroke="#fff" stroke-width="2"/><circle cx="17" cy="11" r="2" fill="#fff"/></svg>
        </span>
        <span class="contact-text"><span class="contact-label">KPV FFL license number</span><span class="contact-value">5-21-XXX-XX-XX-04519</span></span>
      </li>
      <li class="contact-item">
        <span class="contact-icon">
          <svg width="16" height="16" viewBox="0 0 24 24"><path fill="#fff" d="M12 2a7 7 0 0 0-7 7c0 5 7 13 7 13s7-8 7-13a7 7 0 0 0-7-7zm0 9.5A2.5 2.5 0 1 1 12 6.5a2.5 2.5 0 0 1 0 5z"/></svg>
        </span>
        <span class="contact-text"><span class="contact-label">Business address</span><span class="contact-value">412 N Ridgeview Lane #118<br>Linden Hollow, Il 60412</span></span>
      </li>
    </ul>
  </section>

</main>
</body>
</html>
```